DEADLINE 4 JAN 2015 - Drama Movie POSTER

Title of movie " KORAL " - in English SUNSET, Koral is a Sanskrit language, we expect the font to be a little towards that influence ( ethnic )

STORY:
This movie is about one girl's life survival, played by actress ( MIRA HALVORSEN ) fighting her life out of leukemia, deceived in relationship, denying love, searching for her birth father and later kidnapped but saved.

GENRE:
Its a drama with twist of thriller in the end.

COUNTRIES INVOLVED:
Phuket islands in Thailand and Bali and city scenes in Jakarta, Singapore and Istanbul.

We upload photos of actors involved, and we CAN have them on the poster, you can be creative but yet keep it elegant and sophisticated, the movie is for an upmarket. So we dont want too much color. Sunset color mixed with dark or black is nice.

Look forward to see you creative design! Thanks so much!

ACTORS NAME:
- Rudy Pelangi
- Kit B Mayhew
- Tobias Wen
- K Trax
- Hendra Sulut
- Mateo Brunvelli
- Mira Halvorsen
- Sari Lynne
- Ayu Kemalasari
- Ruqaya
- Felix Moro
- Yos Latuheru
- Faustino Medeira

TITLE OF MOVIE:
KORAL - " we love, we cry, we fall but we survive "

If you need sample of promotional trailer, please request with your email address.

Please Check our Brief as we have edited and add some more information needed.Many thanks and look forward to your arts.Warm Regards,KorvoStage Pictures Added Sunday, December 21, 2014

Investors, Young Adults and Adults Crowds

Movie

• Ethnic

• Movie title and Quotes : " we love, we cry, we fall but we survive "
• ( with or without logo ) Production House:
• KorvoStage Pictures in collaboration with Glimmerax.Inc
• Director's name:
• Budi Sastro & Teguh Rambukasih
• Actor Names in order:
• Rudy Pelangi, Ktrax, Sari Lynne, Hendra Sulut, Tobias Wen, Ayu Kemalasari, Felix Moro, Kit B Mayhew, Ruqaya, Mateo Brunvelli, Yos Latuheru, Mira Halvorsen, Faustino Medeira
• Poster influences: Fallow Ridge
• If you want to use the same idea, you can use a silhouette of a girl
• from one of mira halvorsen's picture WITHOUT exposing her face

```html
<!DOCTYPE html>
<html lang="en">
<head>
<meta charset="utf-8">
<title>Koral – Film Poster</title>
<link rel="stylesheet" href="https://fonts.googleapis.com/css2?family=Audiowide&family=Questrial&display=swap">
<style>
  :root {
    --page: #e9e9e9;
    --ink: #1a0d08;
    --ink-soft: #2a160c;
    --gold: #b89656;
    --gold-light: #e8cf98;
    --glow: #fff6e0;
    --shadow: #1c0f08;
  }
  * { margin: 0; padding: 0; box-sizing: border-box; }
  html, body { width: 1200px; height: 1200px; overflow: hidden; }
  body { background: var(--page); font-family: "Questrial", sans-serif; }

  .poster {
    position: absolute;
    left: 230px; top: 52px;
    width: 740px; height: 1096px;
    overflow: hidden;
    color: var(--ink);
    background:
      radial-gradient(circle at 190px 470px, var(--glow) 0%, rgba(255,240,205,.85) 9%, rgba(232,207,152,.55) 26%, rgba(184,150,86,0) 55%),
      radial-gradient(ellipse at 60% 40%, var(--gold-light) 0%, var(--gold) 55%, #6e5430 100%);
  }
  .poster::after {
    content: "";
    position: absolute; inset: 0;
    background:
      linear-gradient(to bottom, rgba(28,15,8,.55) 0%, rgba(28,15,8,0) 22%, rgba(28,15,8,0) 70%, rgba(28,15,8,.75) 100%),
      linear-gradient(to right, rgba(28,15,8,.35) 0%, rgba(28,15,8,0) 30%, rgba(28,15,8,0) 80%, rgba(28,15,8,.35) 100%);
    pointer-events: none;
  }

  .silhouette {
    position: absolute;
    left: 0; top: 0;
    width: 330px; height: 1096px;
    background:
      radial-gradient(ellipse at 70% 48%, rgba(255,246,224,.55) 0%, rgba(255,246,224,0) 35%),
      linear-gradient(to bottom, rgba(90,60,35,.35) 0%, rgba(120,85,50,.15) 40%, rgba(45,24,14,.75) 72%, rgba(28,15,8,.95) 100%);
    border-radius: 0 50% 40% 0 / 0 30% 20% 0;
    z-index: 1;
  }

  .credits { position: absolute; z-index: 2; right: 73px; text-align: right; }
  .directors { top: 308px; font-size: 12px; line-height: 23px; }

  .title {
    position: absolute; z-index: 2;
    right: 70px; top: 388px;
    font-family: "Audiowide", sans-serif;
    font-size: 134px;
    line-height: 1;
    letter-spacing: 4px;
    color: var(--ink);
  }

  .tagline {
    position: absolute; z-index: 2;
    right: 73px; top: 553px;
    text-align: right;
    font-size: 28px;
    line-height: 37px;
    color: var(--ink-soft);
  }

  .cast {
    position: absolute; z-index: 2;
    left: 388px; width: 300px; top: 744px;
    text-align: center;
    font-size: 14.5px;
    line-height: 18.8px;
    color: var(--ink-soft);
  }

  .studio {
    position: absolute; z-index: 3;
    left: 522px; width: 200px;
    text-align: center;
    color: var(--ink);
  }
  .studio-main { top: 914px; }
  .studio-mark {
    width: 38px; height: 38px;
    border-radius: 50%;
    background: var(--ink);
    margin: 0 auto 6px;
  }
  .studio-name { font-size: 13px; letter-spacing: 1px; line-height: 16px; }
  .studio-note { top: 1004px; font-size: 7px; color: var(--gold-light); opacity: .8; }
  .studio-partner {
    top: 1056px;
    display: flex; align-items: center; justify-content: center; gap: 6px;
    font-size: 11px; letter-spacing: 1px; color: var(--gold-light);
  }
  .studio-partner .dot { width: 14px; height: 14px; border-radius: 50%; background: var(--gold-light); }
</style>
</head>
<body>
  <main class="poster">
    <div class="silhouette" role="img" aria-label="Back-lit silhouette of a young woman seen from behind, face hidden, glowing in sunset light"></div>

    <p class="credits directors">Directors<br>Budi Sastro &amp; Teguh Rambukasih</p>

    <h1 class="title">KORAL</h1>

    <p class="tagline">we love<br>we cry<br>we fall<br>but we survive</p>

    <p class="cast">
      Rudy Pelangi • Ktrax • Sari Lynne<br>
      Hendra Sulut • Tobias Wen • Ayu Kemalasari<br>
      Felix Moro • Kit B Mayhew • Ruqaya<br>
      Mateo Brunvelli • Yos Latuheru<br>
      Mira Halvorsen • Faustino Medeira
    </p>

    <div class="studio studio-main">
      <div class="studio-mark"></div>
      <p class="studio-name">KorvoStage Pictures</p>
    </div>
    <p class="studio studio-note">in collaboration with</p>
    <div class="studio studio-partner">
      <span class="dot"></span><span>Glimmerax.Inc</span>
    </div>
  </main>
</body>
</html>
```